IT company website design

Require a home page and an inner page designed for a company located in Ohio. The company deals with a wide range of IT services like Software development, IT based education services such as digital textbooks and BPO

Would like to get a Home page for the website and an inner page to be designed.

Design must be modern, clean and very professional. The home page should have a carousel of our services for which content will be provided.

It should give a feel that we are a large company to our prospective customers.
Updates

Hi,
In the few designs I have got for the home page, there are mockups with unwanted content/blocks like ex. latest blog posts or similar blocks. Kindly note that, we don't want this. Please follow the information about content on the home page as mentioned in the project brief. Designers, who have already submitted designs, if you can remove the unwanted blocks, it will be really appreciated.

Thanks.

I have received over 9 designs for this project, but none of them seem to be custom designed for my needs. They are just re-use of previous designs and look very out dated. Looking for fresh, clean designs following latest design trends like the ones you see in pixelbazaar etc.

If you can provide me a design that meets my expectations, I can definitely UP my budget for you .

Industry/Entity Type

Education

Requirements
Must have
• > > Home page > >
Home page will have

* Top Menu: Home, About Us, Solutions, Services, Contact us (should have space to accommodate for more)

* Should have a flash carousel/slide show. Each slide should be about a service we provide. Ex. a slide for bpo will have the content "Bridging the quality and cost divide in outsourcing" It should be depicted by an illustration or photograph. If you are going to use photograph, please use ones for framelode.com

* Textual content of about 200 words which we will provide

* Links in the footer along with a copyright, legal notice etc.

* Importantly, the home page should have 2 fancy buttons for "Member Login" and "Online Tutoring"

> > Inner pages > >
Will be mainly textual content explaining each of the service so, should have space for lots of textual content, with a fancy, page title (usually the service name). All inner pages should also have a side menu or something like that from where users can have a one click access to all our services.

Our logo is blue in color. with color code "0080FB". It just a stylized D with rest of the text i.e Quorvane Tech Inc. our logo is of the proportion. 1:5 i.e 60px height, 300px wide. We can proportionately increase or decrease the dimensions as necessary. Color combination of the sight should be something that will go with this.

```html
<!DOCTYPE html>
<html lang="en">
<head>
<meta charset="utf-8">
<title>About Us – Quorvane, Inc</title>
<link href="https://fonts.googleapis.com/css2?family=Carlito:ital,wght@0,400;0,700&family=Arimo:wght@400&display=swap" rel="stylesheet">
<style>
  :root {
    --page-bg: #f4f4f4;
    --band-top: #d3e3ec;
    --band-bottom: #72b8f8;
    --brand-blue: #0080fb;
    --nav-blue: #1560b8;
    --title-blue: #1a8ce6;
    --text: #3f3f3f;
    --panel-frame: #ffffff;
    --panel-fill: #e8f6fd;
    --orange-light: #ffa94a;
    --orange-dark: #ff7d10;
    --bullet-red: #d0203a;
    --footer-bg: #cfe1ea;
    --footer-link: #0a6fd8;
    --button-bg-top: #f2f9fd;
    --button-bg-bottom: #cfe7f6;
    --button-border: #a9cfe6;
  }
  * { box-sizing: border-box; margin: 0; padding: 0; }
  html, body { width: 1200px; height: 972px; overflow: hidden; }
  body {
    position: relative;
    background: var(--page-bg);
    font-family: "Carlito", "Calibri", sans-serif;
    color: var(--text);
  }
  .sky-band {
    position: absolute; left: 0; top: 80px; width: 1200px; height: 338px;
    background: linear-gradient(to bottom, var(--band-top) 0%, #b9d7ef 45%, var(--band-bottom) 100%);
  }
  .header-edge { position: absolute; left: 0; top: 70px; width: 1200px; height: 26px; }
  .brand {
    position: absolute; left: 143px; top: 26px; display: flex; align-items: center; gap: 12px;
  }
  .brand-mark { width: 50px; height: 46px; border-radius: 50%; background: var(--brand-blue); }
  .brand-name { font-size: 25px; font-weight: 700; color: var(--brand-blue); }
  .main-nav { position: absolute; top: 0; left: 545px; height: 120px; }
  .main-nav a {
    position: absolute; top: 40px; font-size: 17px; color: var(--nav-blue);
    text-decoration: none; white-space: nowrap;
  }
  .main-nav .active {
    top: 0; left: 106px; width: 83px; height: 118px; padding-top: 40px;
    text-align: center; color: #fff;
    background: linear-gradient(to bottom, var(--orange-light), var(--orange-dark));
    clip-path: polygon(0 0, 100% 0, 100% 92%, 50% 100%, 0 92%);
  }
  .quick-buttons { position: absolute; top: 122px; left: 733px; display: flex; gap: 11px; }
  .quick-button {
    display: flex; align-items: center; gap: 6px; height: 40px; padding: 0 10px 0 4px;
    background: linear-gradient(var(--button-bg-top), var(--button-bg-bottom));
    border: 1px solid var(--button-border); border-radius: 5px;
    font-size: 18px; color: #2b2b2b; text-decoration: none;
  }
  .quick-button .icon {
    width: 32px; height: 32px; border-radius: 3px;
    background: linear-gradient(var(--orange-light), var(--orange-dark));
    display: flex; align-items: center; justify-content: center;
  }
  .content-frame {
    position: absolute; left: 145px; top: 192px; width: 923px; height: 653px;
    background: var(--panel-frame); box-shadow: 0 1px 4px rgba(0,0,0,.18); padding: 9px;
  }
  .content {
    width: 905px; height: 635px; background: var(--panel-fill);
    padding: 17px 11px 0 20px; font-size: 14.6px; line-height: 18px;
  }
  .page-title { font-size: 28px; font-weight: 400; color: var(--title-blue); line-height: 30px; margin-bottom: 12px; }
  .content p { text-align: justify; }
  .feature { display: flex; margin: 21px 0 15px; }
  .feature-photo {
    width: 380px; height: 193px; flex: none;
    background: linear-gradient(135deg, #eef2f5 0%, #c8d6e6 55%, #9fb4cc 100%);
  }
  .feature-list { padding-left: 18px; }
  .feature-list h2 { font-size: 14.6px; font-weight: 700; color: var(--title-blue); margin: 1px 0 14px; }
  .feature-list ul { list-style: none; }
  .feature-list li { position: relative; padding-left: 15px; line-height: 24px; }
  .feature-list li::before { content: "›"; position: absolute; left: 0; color: var(--bullet-red); }
  .content .follow { padding: 0 11px 0 1px; margin-bottom: 18px; }
  .footer-edge { position: absolute; left: 0; top: 885px; width: 1200px; height: 26px; }
  .site-footer {
    position: absolute; left: 0; top: 906px; width: 1200px; height: 66px;
    background: var(--footer-bg); font-family: "Arimo", Arial, sans-serif;
  }
  .footer-nav { position: absolute; left: 134px; top: 11px; font-size: 12px; color: #111; }
  .footer-nav a { color: #111; text-decoration: none; }
  .footer-nav span { margin: 0 7px; }
  .copyright { position: absolute; left: 134px; top: 37px; font-size: 11px; color: #111; }
  .copyright a { color: var(--footer-link); font-size: 12px; margin-left: 4px; }
</style>
</head>
<body>
  <div class="sky-band"></div>
  <svg class="header-edge" viewBox="0 0 1200 26" preserveAspectRatio="none" aria-hidden="true">
    <defs>
      <pattern id="zigzag-down" width="10" height="26" patternUnits="userSpaceOnUse">
        <polygon points="0,0 10,0 10,18 5,24 0,18" fill="#f4f4f4"/>
      </pattern>
    </defs>
    <rect width="1200" height="26" fill="url(#zigzag-down)"/>
  </svg>

  <header>
    <div class="brand"><span class="brand-mark"></span><span class="brand-name">Quorvane, Inc</span></div>
    <nav class="main-nav">
      <a href="#" style="left:23px">Home</a>
      <a href="#" class="active">About Us</a>
      <a href="#" style="left:228px">Solutions</a>
      <a href="#" style="left:341px">Services</a>
      <a href="#" style="left:447px">Contact us</a>
    </nav>
    <div class="quick-buttons">
      <a href="#" class="quick-button" style="width:162px">
        <span class="icon"><svg width="22" height="22" viewBox="0 0 22 22" fill="none" stroke="#fff" stroke-width="2.4"><path d="M9 3h10v16H9"/><path d="M14 11H3M7 7l-4 4 4 4"/></svg></span>Member Login
      </a>
      <a href="#" class="quick-button" style="width:163px">
        <span class="icon"><svg width="22" height="22" viewBox="0 0 22 22" fill="none" stroke="#fff" stroke-width="2.4"><rect x="3" y="3" width="16" height="12"/><path d="M11 15v4M6 19h10"/></svg></span>Online Tutoring
      </a>
    </div>
  </header>

  <main class="content-frame">
    <div class="content">
      <h1 class="page-title">About us</h1>
      <p>Ut erat mi, condimentum viverra condimentum ac, ultricies molestie enim. Fusce odio diam, eleifend feugiat hendrerit eget, ullamcorper ac odio. Praesent sit amet augue ante, eget pulvinar dui. <strong>Curabitur at sollicitudin velit</strong>. Proin tincidunt sodales orci. Nunc nec risus et mauris posuere pretium. Praesent eget metus arcu. Pellentesque id augue ante, et dignissim urna. Vestibulum ante ipsum primis in faucibus orci luctus et ultrices posuere cubilia Curae; Morbi faucibus vestibulum nibh et tincidunt. Sed ac risus in sapien adipiscing eleifend at non ante. Praesent in massa vitae magna bibendum ornare vitae vitae sem. Pellentesque consequat viverra lectus. Nam sed diam eu nibh elementum mattis quis non est. Integer a lectus eget lorem dignissim mattis sit amet sed odio. Morbi lacinia scelerisque leo sit amet suscipit</p>

      <section class="feature">
        <div class="feature-photo" role="img" aria-label="Photo of a smiling business team standing with arms crossed in a bright office"></div>
        <div class="feature-list">
          <h2>Phasellus ultricies fringilla turpis, sit amet cursus dui blandit</h2>
          <ul>
            <li>Lorem ipsum dolor sit amet, consectetur adipiscing elit.</li>
            <li>Fusce fermentum urna bibendum magna commodo posuere.</li>
            <li>Etiam accumsan ipsum in libero vehicula suscipit.</li>
            <li>Ut volutpat magna id nulla mollis id porta mi posuere.</li>
            <li>Aenean vestibulum ligula a dolor dapibus malesuada.</li>
            <li>Donec pulvinar tristique ante, non volutpat arcu dapibus id.</li>
            <li>Pellentesque in augue quis nisl euismod fringilla vel blandit neque.</li>
          </ul>
        </div>
      </section>

      <p class="follow">Lorem ipsum dolor sit amet, consectetur adipiscing elit. Ut in lorem erat, eu convallis arcu. Praesent ligula est, semper a congue vitae, dignissim a orci. Proin condimentum euismod nulla, vitae laoreet justo tempor tincidunt. Vestibulum nec malesuada ligula. Cras sodales eros ac nisi ornare dignissim. In gravida elit at mi viverra nec malesuada arcu auctor.</p>
      <p class="follow">Duis posuere vulputate nisl, ac molestie risus cursus vitae. Integer convallis lectus eros, non dapibus magna. Aliquam placerat, nibh at tincidunt commodo, orci ante semper orci, et cursus mauris nunc quis nisi. Etiam in nibh nec orci tempor semper. Maecenas est erat, tincidunt sit amet elementum sed, porta id risus. Praesent malesuada tristique porttitor. Etiam venenatis ultrices arcu, id condimentum orci semper eu. Nulla facilisi. Sed a leo velit, ac auctor sapien. Mauris massa nisl, aliquet sed pellentesque et, venenatis at tortor. Curabitur id ligula nisl. Sed sed diam nisi. Nullam laoreet tristique turpis quis fringilla.</p>
    </div>
  </main>

  <svg class="footer-edge" viewBox="0 0 1200 26" preserveAspectRatio="none" aria-hidden="true">
    <defs>
      <pattern id="zigzag-up" width="10" height="26" patternUnits="userSpaceOnUse">
        <polygon points="0,26 10,26 10,12 5,6 0,12" fill="#cfe1ea"/>
      </pattern>
    </defs>
    <rect width="1200" height="26" fill="url(#zigzag-up)"/>
  </svg>
  <footer class="site-footer">
    <nav class="footer-nav">
      <a href="#">Home</a><span>|</span><a href="#">About Us</a><span>|</span><a href="#">Solutions</a><span>|</span><a href="#">Services</a><span>|</span><a href="#">Contact us</a>
    </nav>
    <p class="copyright">copyright 2011 Quorvane Tech Inc. All rights reserved. <a href="#">Privacy Policy</a> | <a href="#">Terms and Policies</a></p>
  </footer>
</body>
</html>
```